Medical Clinic Website - New Private Clinic

We have a basic design for a website. Would like it developed in WORDPRESS. the attached JPG shows the page basic design.

Colours and overall design to be similar

MUST BE WORD PRESS and must allow our company to edit at later date. Images must be licenced for use.

The text to be included is:

Target Market(s)

Medical or GP clinic patients

Industry/Entity Type

Medical

Coding

Coded - Design and coding required

Number of Pages Required

1 page

Colors

Designer to choose colors to be used in the design.

Requirements
Must have
• WORDPRESS and use the attached jpg as a design guide.
• Must be able to allow me to insert link to "ember quill" in the top LEFT CORNER. a button or similar. The ember quill designers will help us with this, but it must have the space

```html
<!DOCTYPE html>
<html lang="en">
<head>
<meta charset="utf-8">
<title>Harbour Lane GP</title>
<link href="https://fonts.googleapis.com/css2?family=Mulish:wght@300;400;600;700&display=swap" rel="stylesheet">
<style>
:root{
  --blue:#2b4ea0;
  --navy:#2e3a8c;
  --green:#7dbb2a;
  --green-dark:#2f7a1d;
  --text:#555a60;
  --muted:#8a8f94;
  --soft:#f5f6f8;
  --band:#f7f7f8;
  --white:#ffffff;
}
*{margin:0;padding:0;box-sizing:border-box}
html,body{width:714px;height:1200px;overflow:hidden;background:var(--white)}
body{font-family:"Mulish",sans-serif;color:var(--text);position:relative}
.abs{position:absolute}

/* header */
.partner-button{left:45px;top:31px;width:106px;height:27px;background:var(--navy);border-radius:4px;color:var(--white);font-size:13px;display:flex;align-items:center;justify-content:center;box-shadow:0 1px 3px rgba(0,0,0,.3)}
.brand{right:44px;top:35px;display:flex;align-items:center;gap:8px;color:var(--blue);font-weight:700;font-size:15px;letter-spacing:.2px;white-space:nowrap}
.brand-dot{width:14px;height:14px;background:var(--green);border-radius:50%}
.contact-icon{width:20px;height:20px;border-radius:50%;background:var(--green);display:flex;align-items:center;justify-content:center}
.booking-label{left:249px;top:28px;font-size:8.5px;font-weight:600;color:#444}
.booking-number{left:249px;top:40px;font-size:14.5px;font-weight:400;color:var(--green-dark);letter-spacing:.4px}
.info-label{font-size:7.5px;font-weight:600;color:#444}
.info-value{font-size:7.5px;font-weight:600;color:var(--blue);margin-top:2px;white-space:nowrap}

/* hero */
.hero{left:0;top:88px;width:714px;height:312px;background:linear-gradient(100deg,#e8ecef 0%,#d7dde2 30%,#c9d6dd 55%,#e4e9ec 80%,#eef1f2 100%)}
.hero-band-blue{left:140px;top:177px;width:420px;height:95px;background:linear-gradient(90deg,rgba(64,150,220,.55),rgba(45,135,215,.85) 50%,rgba(64,150,220,.55));color:var(--white);text-align:center;font-weight:300;font-size:24px;line-height:26px;padding-top:18px;white-space:nowrap}
.hero-band-green{left:90px;top:277px;width:530px;height:54px;background:linear-gradient(90deg,rgba(140,195,50,.3),rgba(140,195,45,.85) 25%,rgba(140,195,45,.85) 75%,rgba(140,195,50,.3));color:var(--white);text-align:center;font-weight:300;font-size:19px;line-height:54px}

/* content */
.photo-frame{background:var(--white);padding:5px;box-shadow:0 2px 6px rgba(0,0,0,.25),10px 10px 0 rgba(0,0,0,.05)}
.photo{width:100%;height:100%}
.section-title{color:var(--blue);font-size:11.6px;font-weight:600;letter-spacing:.1px;white-space:nowrap}
.service-list{list-style:none;font-size:8.8px;line-height:17.6px;color:var(--text)}
.service-list li{position:relative;padding-left:14px}
.service-list li::before{content:"";position:absolute;left:0;top:6px;border-left:4px solid #777;border-top:3px solid transparent;border-bottom:3px solid transparent}
.section-copy{font-size:9px;line-height:20.5px;margin-top:6px}

/* footer */
.footer{left:0;top:1095px;width:714px;height:105px;background:var(--soft);text-align:center}
.footer-notice{margin:25px auto 0;width:590px;color:var(--blue);font-size:7.5px;line-height:12px}
.footer-copy{margin-top:8px;color:var(--muted);font-size:7px}
.footer-mail{margin-top:8px}
</style>
</head>
<body>

<!-- header -->
<a class="abs partner-button">Ember Quill</a>

<div class="abs contact-icon" style="left:221px;top:33px">
  <svg width="11" height="11" viewBox="0 0 24 24"><path fill="#fff" d="M6.6 10.8a15 15 0 0 0 6.6 6.6l2.2-2.2a1 1 0 0 1 1-.25 11.4 11.4 0 0 0 3.6.57 1 1 0 0 1 1 1V20a1 1 0 0 1-1 1A17 17 0 0 1 3 4a1 1 0 0 1 1-1h3.5a1 1 0 0 1 1 1c0 1.25.2 2.45.57 3.57a1 1 0 0 1-.25 1z"/></svg>
</div>
<div class="abs booking-label">TO MAKE BOOKING:</div>
<div class="abs booking-number">RING 6150 2731</div>

<div class="abs contact-icon" style="left:385px;top:21px">
  <svg width="11" height="11" viewBox="0 0 24 24"><path fill="#fff" d="M12 3 2 12h3v8h5v-6h4v6h5v-8h3z"/></svg>
</div>
<div class="abs" style="left:410px;top:21px">
  <div class="info-label">ADDRESS:</div>
  <div class="info-value">18 Harbour Lane Eastbrook</div>
</div>
<div class="abs contact-icon" style="left:385px;top:53px">
  <svg width="11" height="11" viewBox="0 0 24 24"><path fill="#fff" d="M3 6h18v12H3z"/><path fill="none" stroke="#7dbb2a" stroke-width="2" d="m3 6 9 7 9-7"/></svg>
</div>
<div class="abs" style="left:410px;top:53px">
  <div class="info-label">EMAIL:</div>
  <div class="info-value">reception@harbourlanegp.com</div>
</div>

<div class="abs brand"><span class="brand-dot"></span>Harbour Lane GP</div>

<!-- hero -->
<div class="abs hero" role="img" aria-label="Doctor showing a tablet to a patient in a bright consulting room"></div>
<div class="abs hero-band-blue">Do you need a doctor's appointment?<br>We are happy to help</div>
<div class="abs hero-band-green">Located in harbour lane eastbrook</div>

<!-- soft background band -->
<svg class="abs" style="left:0;top:580px" width="714" height="515" viewBox="0 0 714 515">
  <polygon points="0,20 714,0 714,515 0,515" fill="#f7f7f8"/>
</svg>

<!-- services -->
<div class="abs photo-frame" style="left:45px;top:428px;width:287px;height:189px">
  <div class="photo" role="img" aria-label="Stethoscope resting on a clipboard with clinic staff in the background" style="background:linear-gradient(160deg,#dfe9f2,#a9c6e0 45%,#eaf1f7)"></div>
</div>
<div class="abs" style="left:366px;top:423px;width:312px">
  <div class="section-title">WE PROVIDE A RANGE OF SERVICES INCLUDING</div>
  <ul class="service-list" style="margin-top:5px;width:300px">
    <li>Chronic conditions such as diabetes, asthma COPD, heart and kidney disease.</li>
    <li>Wound management and dermatology individualised health care</li>
    <li>planning</li>
    <li>Health promotion activities (cholesterol and blood sugar checking, smoking ceasation)</li>
    <li>Work related injury management or treatments</li>
    <li>Travel health and immunisations</li>
    <li>Mental health</li>
    <li>Motor vehicle injury assessments</li>
  </ul>
</div>

<!-- diagnostics -->
<div class="abs" style="left:45px;top:699px;width:312px">
  <div class="section-title">DIAGNOSTIC SERVICES INCLUDING PATHOLOGY</div>
  <p class="section-copy">We can collect samples including blood, urine and drug and alcohol tests at our clinic. Our plan is to open a formal collection centre with the practice.</p>
</div>
<div class="abs photo-frame" style="left:383px;top:648px;width:287px;height:185px">
  <div class="photo" role="img" aria-label="Gloved hand placing blood sample tubes in a laboratory rack" style="background:linear-gradient(150deg,#d8e6ef,#b8c8de 40%,#8f8fc8 70%,#e6ecf2)"></div>
</div>

<!-- physiotherapy -->
<div class="abs photo-frame" style="left:45px;top:868px;width:287px;height:189px">
  <div class="photo" role="img" aria-label="Physiotherapist helping an older patient walk along parallel bars" style="background:linear-gradient(160deg,#eef0f2,#d9dfe4 50%,#a7c9b8 85%,#8fb7a8)"></div>
</div>
<div class="abs" style="left:366px;top:924px;width:295px">
  <div class="section-title">PHYSIOTHERAPY SERVICES</div>
  <p class="section-copy">We are currently looking for a physiotherapy partner for our clinic. In the near future we will be giving more details about this service.</p>
</div>

<!-- footer -->
<div class="abs footer">
  <p class="footer-notice">If you are experiencing any chest pain, difficulty with breathing or any acute symptoms associated with the heart, lungs, or the brain, please go to your nearest hospital or call the Cityline Ambulance on 000 immediately. Do not wait in the waiting room.</p>
  <p class="footer-copy">Copyright © 2017. Company Name. All Right Reserved</p>
  <div class="footer-mail">
    <svg width="16" height="12" viewBox="0 0 16 12"><rect width="16" height="12" rx="1" fill="#8a8f94"/><path d="M0 1l8 6 8-6" fill="none" stroke="#f5f6f8" stroke-width="1.3"/></svg>
  </div>
</div>

</body>
</html>
```